Elmcrest Louvres Website Redesign

Looking for an updated design to our Wordpress website based upon our new logo. We are looking for something that is consumer friendly, shows sophistication and is pleasing to the eye.

About us - We are in the Window Coverings business. We manufacture Plantation Shutters, Blinds, Barn Doors and Draperies. Our current website can be found at http://www.elmcrestlouvres.example

Target Market(s)

Consumers that go to the website to see the product and learn about the services we offer.

Industry/Entity Type

Consumer

Coding

Coded - Design and coding required

Requirements
Should not have
• We do not do ecommerce at this point in time.

```html
<!DOCTYPE html>
<html lang="en">
<head>
<meta charset="utf-8">
<title>Elmcrest Louvres — Window Treatments</title>
<link href="https://fonts.googleapis.com/css2?family=Jost:wght@300;400;500;600&family=Lora:wght@400;500&display=swap" rel="stylesheet">
<style>
:root{
  --green:#80bc41;
  --green-dark:#6aa32f;
  --slate:#4a4f5a;
  --slate-dark:#3f434d;
  --beige:#eeeee2;
  --beige-card:#efefe4;
  --ink:#3a3d44;
  --muted:#6f737b;
  --line:#d8d8d8;
  --white:#ffffff;
  --serif:'Lora',Georgia,serif;
  --sans:'Jost','Century Gothic',sans-serif;
}
*{box-sizing:border-box;margin:0;padding:0}
html,body{width:1200px;height:3321px;overflow:hidden}
body{position:relative;font-family:var(--sans);color:var(--ink);background:var(--white)}
.abs{position:absolute}
a{color:inherit;text-decoration:none}

.backdrop-photo{left:0;top:0;width:1200px;height:742px;background:linear-gradient(90deg,#d9dcd6 0%,#eceeea 30%,#f3f4f1 60%,#dfe4da 85%,#cdd6c3 100%)}
.backdrop-band{left:0;top:742px;width:1200px;height:498px;background:var(--beige)}

.site-header{left:155px;top:49px;width:890px;height:119px;background:var(--white)}
.brand{left:25px;top:22px;display:flex;align-items:center;gap:9px}
.brand-mark{width:30px;height:30px;border:3px solid var(--green);border-radius:4px}
.brand-name{font-family:var(--sans);font-size:26px;font-weight:500;color:var(--green)}
.appointment{left:290px;top:28px;font-size:14px;color:var(--green);font-weight:500}
.appointment b{color:var(--ink);font-weight:500;margin-left:6px}
.socials{display:flex;gap:6px}
.socials span{width:25px;height:25px;border:1.5px solid #8d9096;border-radius:50%;display:block}
.socials .on{background:var(--green);border-color:var(--green)}
.site-header .socials{left:608px;top:22px}
.nav{left:0;top:78px;width:890px;height:27px;border-bottom:1px solid var(--line);display:flex;font-size:13px;color:var(--ink)}
.nav a{position:relative;height:27px;line-height:14px}
.nav .active{color:var(--green)}
.nav .active::after{content:"";position:absolute;left:-6px;right:-6px;bottom:-1px;height:2px;background:var(--green)}

.hero{left:155px;top:168px;width:890px;height:399px;background:linear-gradient(120deg,#5a3b26 0%,#8a6446 30%,#c8a783 50%,#7b5436 72%,#4b2f1d 100%)}
.hero-title{left:0;width:890px;top:128px;text-align:center;font-family:var(--serif);font-weight:400;color:var(--white);font-size:32px;line-height:40px}
.hero-title .big{font-size:34px}
.btn{display:inline-block;background:var(--green);color:var(--white);border-radius:16px;font-size:13px;font-weight:500;text-align:center}
.hero .btn{position:absolute;left:361px;top:232px;width:168px;height:32px;line-height:32px}
.slider-arrow{top:345px}

.cat{top:591px;width:303px;height:248px;background:var(--white)}
.cat-photo{width:100%;height:151px;background:linear-gradient(135deg,#e3e1dc,#b9b3aa 60%,#6d655c)}
.cat.raised{top:586px;box-shadow:0 6px 14px rgba(0,0,0,.18)}
.cat.raised .cat-photo{background:linear-gradient(135deg,#a6d46e,#80bc41 60%,#6aa32f)}
.cat h3{font-family:var(--serif);font-weight:400;color:var(--green);font-size:16px;text-align:center;margin-top:28px}
.cat p{font-size:12px;color:var(--muted);text-align:center;margin-top:3px}

.promo{left:0;width:1200px;top:884px;text-align:center}
.promo h2{font-family:var(--serif);font-weight:400;font-size:22px;color:var(--ink)}
.promo h2 span{color:var(--green)}
.promo p{font-size:16px;line-height:22px;margin-top:12px}
.promo .btn{margin-top:20px;width:263px;height:33px;line-height:33px}

.process{left:155px;top:1083px;width:890px;height:316px;background:#f4f4f2}
.tab{left:0;width:303px;height:76px;display:flex;align-items:center;padding-left:84px;font-family:var(--serif);font-size:16px;color:var(--white)}
.tab svg{position:absolute;left:24px;top:20px}
.tab.dark{background:var(--slate)}
.tab.plain{background:var(--white);color:var(--ink)}
.tab.green{background:var(--green)}
.process h3{left:333px;top:44px;font-family:var(--serif);font-weight:400;font-size:22px}
.rule{height:1px;background:#9a9da3}
.process .text{left:333px;top:114px;width:310px;font-size:12.5px;line-height:19px;color:var(--muted)}
.process-photo{left:686px;top:24px;width:180px;height:270px;background:linear-gradient(160deg,#d7d3cc,#a9a197 55%,#7e776e)}

.about h2,.testimonial h2,.news h2{font-family:var(--serif);font-weight:400;font-size:22px;color:var(--ink)}
.about{left:155px;top:1446px;width:565px}
.about .lead{margin-top:14px;font-size:13px;line-height:19px;color:var(--ink)}
.about p{font-size:13px;line-height:19px;color:var(--muted);margin-top:12px}
.about .btn{margin-top:20px;width:144px;height:30px;line-height:30px}
.form{left:764px;top:1450px;width:281px;height:321px;background:var(--green);padding:14px 10px 10px 12px}
.form-inner{width:100%;height:100%;background:var(--white);padding:34px 24px 0 24px;text-align:center}
.form h3{font-family:var(--serif);font-weight:400;font-size:17px}
.form small{display:block;font-size:13px;color:var(--muted);margin-top:2px}
.field{margin-top:11px;height:32px;border:1px solid #cfd0d3;text-align:left;padding-left:12px;line-height:30px;font-size:11px;color:var(--muted)}
.form .field:first-of-type{margin-top:28px}
.btn-dark{display:inline-block;margin-top:22px;width:146px;height:32px;line-height:32px;border-radius:16px;background:var(--slate);color:var(--white);font-size:12px;font-weight:500}

.testimonial{left:155px;top:1876px;width:260px}
.testimonial p{margin-top:12px;font-size:12.5px;line-height:17px;color:var(--muted)}
.testimonial a{display:inline-block;margin-top:14px;font-size:12px;color:var(--muted);text-decoration:underline}
.quote-box{left:434px;top:1842px;width:558px;height:190px;border:1px solid #dcdcdc;background:var(--white)}
.quote-box blockquote{position:absolute;left:38px;top:20px;width:490px;font-size:15px;line-height:21px;color:var(--muted)}
.quote-box cite{position:absolute;left:38px;top:122px;font-family:var(--serif);font-style:normal;font-size:15px;color:var(--ink)}
.quote-mark{left:412px;top:1960px;width:46px;height:46px;background:var(--white);border:1px solid #dcdcdc}
.circle-btn{width:32px;height:32px;border-radius:50%;border:1.5px solid #b9bcc0;background:var(--white)}
.circle-btn.on{background:var(--green);border-color:var(--green)}

.banner{left:0;top:2081px;width:1200px;height:377px;background:linear-gradient(90deg,#2b1c14 0%,#5d4130 35%,#3a2a20 60%,#6a4e3a 85%,#2c1f17 100%)}
.banner-frame{left:84px;top:51px;width:1032px;height:277px;border:2px solid var(--white)}
.banner-text{left:0;width:1200px;text-align:center;color:var(--white);font-family:var(--serif)}
.banner .hello{top:88px;font-size:26px}
.banner .event{top:152px;font-size:44px;color:var(--green)}
.banner .buy{top:203px;font-size:38px}
.banner .buy span{color:var(--green)}
.banner .cta{top:263px;font-family:var(--sans);font-size:16px;font-weight:600;text-decoration:underline}

.news{left:155px;top:2500px;width:890px}
.news h2 span{color:var(--green)}
.news .view{position:absolute;right:0;top:12px;font-size:12px;color:var(--ink);text-decoration:underline}
.news-card{top:2557px;width:281px;height:266px;background:var(--beige-card)}
.news-card.raised{background:var(--white);box-shadow:0 4px 12px rgba(0,0,0,.16)}
.news-photo{height:162px}
.news-card h4{font-size:13px;font-weight:500;text-align:center;line-height:18px;margin-top:26px;padding:0 26px}
.news-card .circle-btn{position:absolute;left:124px;bottom:-16px}

.footer{left:0;top:2889px;width:1200px;height:432px;background:var(--slate)}
.f-col{top:44px;font-size:12px;line-height:24px;color:#d8dade}
.f-col h5{font-size:13px;font-weight:500;color:var(--green);line-height:20px;margin-bottom:7px;padding-bottom:4px;border-bottom:1px solid #6a6f79}
.f-col .u{text-decoration:underline}
.f-brand{left:764px;top:58px;display:flex;align-items:center;gap:10px}
.f-brand .brand-mark{width:40px;height:40px}
.f-brand .brand-name{font-size:32px;color:var(--white)}
.f-contact{left:764px;top:116px;font-size:14px;line-height:29px;color:var(--white)}
.f-contact b{color:var(--green);font-weight:500}
.footer .socials{left:764px;top:200px}
.footer .socials span{border-color:#b7bac0}
.badges{left:764px;top:262px;display:flex;gap:22px;align-items:center}
.f-bottom{left:155px;top:370px;width:890px;border-top:1px solid #666b75;padding-top:24px;font-size:11px;color:#c3c6cc}
</style>
</head>
<body>

<div class="abs backdrop-photo" role="img" aria-label="Softly blurred bright living room with a window and a potted plant"></div>
<div class="abs backdrop-band"></div>

<header class="abs site-header">
  <div class="abs brand"><span class="brand-mark"></span><span class="brand-name">Elmcrest</span></div>
  <div class="abs appointment">Make An Appointment: <b>1-800-555-0142</b></div>
  <div class="abs socials"><span></span><span></span><span class="on"></span><span></span><span></span><span></span><span></span></div>
  <nav class="abs nav">
    <a class="active" style="margin-left:48px">Home</a>
    <a style="margin-left:36px">Our Promise</a>
    <a style="margin-left:36px">Window Treatments</a>
    <a style="margin-left:36px">Photo Gallery</a>
    <a style="margin-left:36px">Where To Buy</a>
    <a style="margin-left:36px">What's New/Savings</a>
    <a style="margin-left:36px">Contact Us</a>
  </nav>
</header>

<section class="abs hero" role="img" aria-label="Warm living room with wooden blinds over tall windows">
  <h1 class="abs hero-title"><span class="big">What's the Best</span><br>Window Treatment for You?</h1>
  <a class="btn">Blinds and Shades</a>
</section>
<svg class="abs slider-arrow" style="left:104px" width="20" height="40" viewBox="0 0 20 40"><path d="M16 4 4 20l12 16" fill="none" stroke="#fff" stroke-width="3"/></svg>
<svg class="abs slider-arrow" style="left:1076px" width="20" height="40" viewBox="0 0 20 40"><path d="M4 4l12 16L4 36" fill="none" stroke="#fff" stroke-width="3"/></svg>

<article class="abs cat" style="left:155px"><div class="cat-photo" role="img" aria-label="Bright room with white blinds"></div><h3>Blinds and Shades</h3><p>Northfield Weave</p></article>
<article class="abs cat raised" style="left:460px"><div class="cat-photo" role="img" aria-label="Room with plantation shutters under a green tint"></div><h3>Shutters</h3><p>Perfect for Any Window</p></article>
<article class="abs cat" style="left:764px"><div class="cat-photo" role="img" aria-label="Living room with draperies"></div><h3>Draperies</h3><p>Curtains and Valances</p></article>

<section class="abs promo">
  <h2><span>Save up to 20% Off</span> Custom, Installed Shutters for Autumn</h2>
  <p><b style="font-weight:500">Call Us: 800-555-0199 or</b> fill out the form to schedule your free<br>in-home design consultation.</p>
  <a class="btn">Free Home Design Consultation</a>
</section>

<section class="abs process">
  <div class="abs tab dark" style="top:0">
    <svg width="40" height="36" viewBox="0 0 40 36" fill="none" stroke="#fff" stroke-width="2"><circle cx="20" cy="16" r="8"/><path d="M16 26h8M17 30h6M20 2v3M8 6l2 2M32 6l-2 2M5 16h3M32 16h3"/></svg>We Design It</div>
  <div class="abs tab plain" style="top:80px">
    <svg width="40" height="36" viewBox="0 0 40 36" fill="none" stroke="#4a4f5a" stroke-width="2.5"><path d="M8 30 26 12M22 6l10 10M6 8l24 24"/></svg>We Make It</div>
  <div class="abs tab dark" style="top:160px">
    <svg width="40" height="36" viewBox="0 0 40 36" fill="none" stroke="#fff" stroke-width="2"><rect x="6" y="8" width="22" height="12" rx="2"/><path d="M28 14h8M12 20l-2 12h8l2-12"/></svg>We Install It</div>
  <div class="abs tab green" style="top:240px">
    <svg width="40" height="36" viewBox="0 0 40 36" fill="none" stroke="#fff" stroke-width="2.2"><path d="M20 32 6 18a8 8 0 0 1 14-10 8 8 0 0 1 14 10Z"/></svg>You'll Love It</div>
  <h3 class="abs">We Make It</h3>
  <div class="abs rule" style="left:333px;top:88px;width:56px"></div>
  <p class="abs text">Elmcrest's shutters are manufactured in our state-of-the-art facility in Texas on proprietary precision-automated equipment and finished with environmentally-friendly waterborne paints, stains and sealers. American-made products mean more than quality assurance. Our lead times are among the fastest in the industry — approximately four weeks.</p>
  <div class="abs process-photo" role="img" aria-label="Craftsperson assembling a shutter panel in the workshop"></div>
</section>

<section class="abs about">
  <h2>About Us <span class="rule" style="display:inline-block;width:80px;vertical-align:middle;margin-left:14px"></span></h2>
  <p class="lead">We are in the Window Coverings business. We manufacture Plantation Shutters, Blinds, Barn Doors and Draperies</p>
  <p>For over 18-years, Elmcrest Louvres has blended traditional craftsmanship with innovative designs to create a beautifully handcrafted plantation shutters, window treatments and our Slim Profile Barn Doors.</p>
  <p>We bring this combination of quality and customization to you through our design consultation process and our commitment to the friendliest customer service…</p>
  <a class="btn">Discover More</a>
</section>

<aside class="abs form">
  <div class="form-inner">
    <h3>Schedule Your Free</h3>
    <small>in-home design consultation.</small>
    <div class="field">Name</div>
    <div class="field">Email</div>
    <div class="field">Phone</div>
    <span class="btn-dark">Get Started</span>
  </div>
</aside>

<section class="abs testimonial">
  <h2>Testimonial <span class="rule" style="display:inline-block;width:44px;vertical-align:middle;margin-left:10px"></span></h2>
  <p>There are many variations<br>of passages of Lorem Ipsum the.</p>
  <a>View All</a>
</section>
<div class="abs quote-box">
  <blockquote>Just wanted to let you know how much we love our shutters. Don't know why we waited so long to get them. Thank you for excellent workmanship and professionalism.</blockquote>
  <cite>Marta and Glen</cite>
</div>
<div class="abs quote-mark"><svg width="46" height="46" viewBox="0 0 46 46" fill="#4a4f5a"><path d="M13 30v-7c0-5 2-8 6-9v3c-2 1-3 3-3 5h3v8zM25 30v-7c0-5 2-8 6-9v3c-2 1-3 3-3 5h3v8z"/></svg></div>
<div class="abs circle-btn" style="left:1011px;top:1904px"><svg width="29" height="29" viewBox="0 0 29 29"><path d="M16 10l-5 4.5 5 4.5" fill="none" stroke="#80bc41" stroke-width="2"/></svg></div>
<div class="abs circle-btn on" style="left:1011px;top:1944px"><svg width="29" height="29" viewBox="0 0 29 29"><path d="M13 10l5 4.5-5 4.5" fill="none" stroke="#fff" stroke-width="2"/></svg></div>

<section class="abs banner" role="img" aria-label="Dim living room at dusk with dark wood blinds and city view">
  <div class="abs banner-frame"></div>
  <div class="abs banner-text hello">Hello Autumn</div>
  <div class="abs banner-text event">Savings Event</div>
  <div class="abs banner-text buy">Buy Now for <span>Holiday Installation</span></div>
  <div class="abs banner-text cta">Receive FREE In-Home Design Consultation</div>
</section>

<section class="abs news">
  <h2><span>Elmcrest</span> News <span class="rule" style="display:inline-block;width:44px;vertical-align:middle;margin-left:10px"></span></h2>
  <a class="view">View All News</a>
</section>
<article class="abs news-card" style="left:155px">
  <div class="news-photo" role="img" aria-label="Autumn leaves promotional graphic" style="background:linear-gradient(135deg,#e0a24a,#c4622a 55%,#8d3d1c)"></div>
  <h4>Autumn Savings on Window Treatments</h4>
  <div class="circle-btn"><svg width="29" height="29" viewBox="0 0 29 29"><path d="M13 10l5 4.5-5 4.5" fill="none" stroke="#80bc41" stroke-width="2"/></svg></div>
</article>
<article class="abs news-card raised" style="left:460px">
  <div class="news-photo" role="img" aria-label="Shade savings flyer with window photos" style="background:linear-gradient(135deg,#eef0f2,#c9cfd6 55%,#8f9aa6)"></div>
  <h4>Savings on Northfield Weave Shades</h4>
  <div class="circle-btn on"><svg width="29" height="29" viewBox="0 0 29 29"><path d="M13 10l5 4.5-5 4.5" fill="none" stroke="#fff" stroke-width="2"/></svg></div>
</article>
<article class="abs news-card" style="left:764px">
  <div class="news-photo" role="img" aria-label="Team standing together holding an award" style="background:linear-gradient(135deg,#6d6f72,#3d3f44 55%,#23252a)"></div>
  <h4>Elmcrest Louvres Receives Pinnacle Award</h4>
  <div class="circle-btn"><svg width="29" height="29" viewBox="0 0 29 29"><path d="M13 10l5 4.5-5 4.5" fill="none" stroke="#80bc41" stroke-width="2"/></svg></div>
</article>

<footer class="abs footer">
  <div class="abs f-col" style="left:155px;width:126px"><h5>Our Promise</h5><div class="u">Consultation Process</div><div>Our Story</div><div>Testimonials</div><div>Warranty</div><div>FAQs</div><div>Careers</div></div>
  <div class="abs f-col" style="left:305px;width:128px"><h5>Shutters</h5><div>Configurations</div><div>Design Basics</div><div>Wood Shutters</div><div>Poly Shutters</div><div>Slimline Shutters</div><div>Arch Windows</div><div>Sliding &amp; French</div><div>Doors</div><div>Café Shutters</div><div>Classic Shutters</div></div>
  <div class="abs f-col" style="left:458px;width:128px"><h5>Blinds &amp; Shades</h5><div>Design Basics</div><div>Vertical Options</div><div>Horizontal Blinds</div><div>Honeycomb Cellular</div><div>Woven Wood</div><div>Roman Shades</div><div>Sheer Shades</div><div>Roller Shades</div></div>
  <div class="abs f-col" style="left:611px;width:120px"><h5>Draperies</h5><div>Design Basics</div><div>Sheer Draperies</div><div>Lined Draperies</div><div>Decorative Side</div><div>Panels</div><div>Top Treatments</div><div>Fabric Shades</div><div>Custom Pillows</div></div>
  <div class="abs f-brand"><span class="brand-mark"></span><span class="brand-name">Elmcrest</span></div>
  <div class="abs f-contact"><div><b>Phone:</b> (800) 555-0199</div><div><b>Email:</b> <span style="text-decoration:underline">hello@elmcrestlouvres.example</span></div></div>
  <div class="abs socials"><span></span><span></span><span class="on"></span><span></span><span></span><span></span><span></span></div>
  <div class="abs badges">
    <span style="width:42px;height:42px;background:#e6b422;display:block"></span>
    <span style="width:80px;height:30px;background:#f2f2f2;display:block"></span>
    <span style="width:90px;height:32px;background:#1f6c93;display:block"></span>
  </div>
  <div class="abs f-bottom">© 2017 Elmcrest. All Right Reserved
    <svg style="position:absolute;right:4px;top:20px" width="16" height="16" viewBox="0 0 16 16"><path d="M8 2 2 10h4v5h4v-5h4z" fill="#80bc41"/></svg>
  </div>
</footer>

</body>
</html>
```